"Each Porch Route" 9x6.5" mailer for church ministry event in park

We are a small church trying to reach out in a relevant way to our community. We want to send a postcard ad to all the houses on the surrounding mail routes via "Each Porch Route" (see NMLX.com for more info or I can provide specs if you do not already have them). Mailer actually needs to be at least 6.25" high. 9x6.5 is the biggest we want to go. Attached docs should provide all the necessary info. Front side of card will have necessary postal stuff in top right and rest should be devoted to our "Main Event" which is the event in the park (see attached info). 2nd biggest event to highlight (front or back) is our Wildwood Bible Club. Our goal is to target families with young kids and encourage them to visit our church for one of these events and want to come back again! Our church website is www.heldenbrook.com. We are a growing family-friendly local church that wants to "help families grow." I have also considered the tag line "helping to make our community more pleasant" because we live in Pleasant Township. I look forward to seeing your ideas!

Families with young children in our local community

Religious

• Brightway Parcel Corp requirements for "Each Porch Route" mailing (nmlx.com); highlight main event on front (plus one more event if space allows); summer "calendar of events on back side plus information about our local church to attract "unchurched" families

```html
<!DOCTYPE html>
<html lang="en">
<head>
<meta charset="utf-8">
<title>Church Ministry Event in Park – Mailer</title>
<link rel="stylesheet" href="https://fonts.googleapis.com/css2?family=Baloo+2:wght@600;700;800&family=Questrial&family=Lato:wght@400;700&display=swap">
<style>
:root{
  --backdrop:#4a3220;
  --white:#ffffff;
  --ink:#1f1f1f;
  --pink:#e3237e;
  --green:#3aab47;
  --yellow:#ffd200;
  --blue:#1d5fb0;
  --sky:#2a8fdc;
  --date-blue:#2b5aa6;
  --gold-a:#f2e24a;
  --gold-b:#c7a81a;
  --calendar:#161616;
  --cal-date:#36a9e1;
  --cal-note:#4fc34a;
}
*{margin:0;padding:0;box-sizing:border-box}
html,body{width:907px;height:1200px;overflow:hidden;background:var(--backdrop)}
.canvas{position:relative;width:907px;height:1200px}
.card{position:absolute;background:var(--white);overflow:hidden}
.card svg.shapes{position:absolute;left:0;top:0}
.front{left:52px;top:44px;width:808px;height:529px}
.back{left:57px;top:603px;width:809px;height:532px}

.family-art{position:absolute;left:73px;top:30px;width:250px;height:172px;border-radius:40px 40px 20px 20px;
  background:linear-gradient(180deg,#cfe6f6 0%,#fdf3c4 55%,#9ccf5a 100%)}
.event-title{position:absolute;left:48px;top:226px;font-family:"Baloo 2",sans-serif}
.event-title .kicker{display:block;color:var(--pink);font-weight:800;font-size:46px;line-height:46px;letter-spacing:-0.5px}
.event-title .main{display:block;color:var(--ink);font-family:"Questrial",sans-serif;font-size:49px;line-height:56px;margin-left:-2px}
.date-bar{position:absolute;left:41px;top:337px;width:340px;height:36px;border-radius:4px;
  background:linear-gradient(180deg,#3a72c4,var(--date-blue));color:var(--white);
  font-family:"Questrial",sans-serif;font-weight:700;font-size:27px;line-height:36px;text-align:center;letter-spacing:0.5px}
.date-bar .year{color:var(--yellow);margin-left:12px;font-family:"Baloo 2",sans-serif;font-weight:700}
.stamp-box{position:absolute;left:706px;top:19px;width:78px;height:90px;border:2px solid var(--ink)}
.address-line{position:absolute;left:600px;width:186px;height:3px;background:var(--ink)}
.info{position:absolute;top:451px;font-family:"Lato",sans-serif;font-size:14px;line-height:18.5px;color:var(--white)}
.info .accent{color:var(--pink)}
.info-when{left:32px}
.info-where{left:195px}

.bounce-photo{position:absolute;left:43px;top:74px;width:166px;height:166px;border-radius:50%;
  background:radial-gradient(circle at 50% 45%,#d9433c 0%,#3d59b8 60%,#f1f1f1 100%)}
.time-badge{position:absolute;left:293px;top:102px;width:104px;height:104px;text-align:center;font-family:"Baloo 2",sans-serif}
.time-badge .label{display:block;color:var(--pink);font-weight:800;font-size:26px;line-height:26px;margin-top:26px}
.time-badge .hours{display:block;color:var(--ink);font-family:"Lato",sans-serif;font-weight:700;font-size:13px}
.promo{position:absolute;right:48px;top:14px;text-align:right;font-family:"Baloo 2",sans-serif}
.promo .lead{display:block;color:var(--yellow);font-weight:800;font-size:20px;line-height:26px}
.promo .club{display:block;color:var(--white);font-family:"Questrial",sans-serif;font-size:26px;line-height:32px}
.promo .dates{display:block;color:var(--pink);font-weight:800;font-size:25px;line-height:30px}
.park-box{position:absolute;top:205px;height:132px;border-radius:0 0 22px 22px;
  background:linear-gradient(180deg,var(--gold-a),var(--gold-b));font-family:"Baloo 2",sans-serif;color:var(--ink);
  font-weight:700;font-size:22px;line-height:25px;padding:46px 0 0 38px}
.park-box.first{left:318px;width:210px}
.park-box.second{left:561px;width:222px;padding-top:36px;padding-left:28px}
.family-sketch{position:absolute;left:25px;top:290px;width:270px;height:210px;border-radius:30px;
  background:linear-gradient(180deg,#f4f4f4,#e6e6e6)}
.calendar{position:absolute;left:315px;top:345px;width:494px;height:116px;background:var(--calendar);
  border-radius:14px 0 0 14px;padding:14px 0 0 19px;font-family:"Lato",sans-serif;font-size:11px;line-height:12.4px;color:var(--white)}
.calendar::before{content:"";position:absolute;inset:5px 0 5px 5px;border:1px dashed rgba(255,255,255,.7);border-right:none;border-radius:10px 0 0 10px}
.calendar .row{position:relative;display:flex;white-space:nowrap}
.calendar .date{color:var(--cal-date);width:54px}
.calendar .what{width:210px}
.calendar .note{color:var(--cal-note)}
.guests{position:absolute;left:368px;top:466px;display:flex;align-items:center;gap:12px;font-family:"Baloo 2",sans-serif}
.partner{display:flex;align-items:center;gap:4px;color:var(--blue);font-weight:700;font-size:12px;line-height:13px;width:62px}
.partner .dot{width:9px;height:9px;background:var(--pink);border-radius:50%;flex:none}
.guests .tagline{color:var(--sky);font-weight:800;font-size:24px;letter-spacing:0.5px;margin-left:6px}
.bottom-bar{position:absolute;left:0;top:510px;width:809px;height:22px;background:var(--pink)}
</style>
</head>
<body>
<div class="canvas">

  <section class="card front">
    <svg class="shapes" width="808" height="529" viewBox="0 0 808 529" aria-hidden="true">
      <path d="M0,428 C130,392 290,392 405,386 C440,450 420,495 385,529 L0,529 Z" fill="var(--calendar)"/>
      <path d="M0,412 C130,378 290,378 425,370" fill="none" stroke="var(--green)" stroke-width="10"/>
      <path d="M440,0 C395,90 380,180 405,260 C430,340 420,440 350,529" fill="none" stroke="var(--green)" stroke-width="16"/>
      <path d="M470,0 C425,95 415,185 440,265 C462,345 445,440 395,529" fill="none" stroke="var(--yellow)" stroke-width="20"/>
      <path d="M505,0 C460,100 450,190 470,270 C488,350 475,445 440,529" fill="none" stroke="var(--pink)" stroke-width="13"/>
      <path d="M528,0 C485,105 475,195 490,275 C505,355 492,450 462,529" fill="none" stroke="var(--blue)" stroke-width="8"/>
    </svg>
    <div class="family-art" role="img" aria-label="Hand-drawn family of four standing on grass under a smiling sun"></div>
    <h1 class="event-title"><span class="kicker">church ministry</span><span class="main">event in park</span></h1>
    <div class="date-bar">26-27June<span class="year">2016</span></div>
    <div class="stamp-box"></div>
    <div class="address-line" style="top:295px"></div>
    <div class="address-line" style="top:321px"></div>
    <div class="address-line" style="top:347px"></div>
    <p class="info info-when"><span class="accent">5:00-8:30pm</span><br>Food provided<br>Bouncy houses</p>
    <p class="info info-where"><span class="accent">Pleasant Park</span><br>2870 Alder Ridge Rd<br>Fairhaven, OH 45999</p>
  </section>

  <section class="card back">
    <svg class="shapes" width="809" height="532" viewBox="0 0 809 532" aria-hidden="true">
      <defs>
        <linearGradient id="sky" x1="0" y1="0" x2="1" y2="0.4">
          <stop offset="0" stop-color="#1f7fd0"/><stop offset="1" stop-color="#37a6e8"/>
        </linearGradient>
      </defs>
      <path d="M0,0 H809 V150 C660,118 470,140 330,210 C220,262 110,262 0,250 Z" fill="url(#sky)"/>
      <path d="M809,138 C650,110 470,132 330,200 C220,252 110,252 0,240" fill="none" stroke="var(--green)" stroke-width="9"/>
      <path d="M809,165 C660,135 480,155 340,222 C230,274 110,274 0,262" fill="none" stroke="var(--pink)" stroke-width="11"/>
      <circle cx="126" cy="157" r="110" fill="var(--white)" stroke="var(--green)" stroke-width="8"/>
      <circle cx="126" cy="157" r="96" fill="none" stroke="var(--pink)" stroke-width="6"/>
      <circle cx="345" cy="154" r="64" fill="var(--white)" stroke="var(--green)" stroke-width="7"/>
      <circle cx="345" cy="154" r="54" fill="none" stroke="var(--pink)" stroke-width="5"/>
    </svg>
    <div class="bounce-photo" role="img" aria-label="Photo of an inflatable bounce castle"></div>
    <div class="time-badge"><span class="label">Time</span><span class="hours">6:30-8:30pm</span></div>
    <div class="promo">
      <span class="lead">The 2nd big thing we want to promote</span>
      <span class="club">is our Wildwood Bible Club</span>
      <span class="dates">Sun July 31-Thu Aug 4</span>
    </div>
    <div class="park-box first">Pleasant Park<br>Sunday June 26<br>4:00 - 8:30pm</div>
    <div class="park-box second">Corwin Park<br>Monday June 27<br>4:00 - 8:30pm</div>
    <div class="family-sketch" role="img" aria-label="Line sketch of a family with children and a dog"></div>
    <div class="calendar">
      <div class="row"><span class="date">June 26</span><span class="what">Pleasant Park w/ Project Lantern</span><span class="note">Invite your friends!!</span></div>
      <div class="row"><span class="date">June 27</span><span class="what">Corwin Park w/ Project Lantern</span><span class="note">Please pray!</span></div>
      <div class="row"><span class="date">July 12</span><span class="what">Academy of Arts @ Heldenbrook Grace</span><span class="note">Bring your family</span></div>
      <div class="row"><span class="date">July 31</span><span>Wildwood Bible Club “Opening Ceremony” @ Heldenbrook Grace</span></div>
      <div class="row"><span class="date">August 11</span><span>Gearhouse Men’s Group “Car Show” @ Heldenbrook Grace</span></div>
      <div class="row"><span class="date">August 27</span><span>Saturday in the Park</span></div>
    </div>
    <div class="guests">
      <span class="partner"><span class="dot"></span>Kinfolk Fun</span>
      <span class="partner"><span class="dot"></span>Project Lantern</span>
      <span class="tagline">with special guests</span>
    </div>
    <div class="bottom-bar"></div>
  </section>

</div>
</body>
</html>
```